hobby beef jerky maker looking to break into the commercial market

We need product labels designed for each flavour of jerky we make. Currently have 3 flavours that we are ready to share with the world. We need in your face designs to help us stand out from an already crowded market.
The product name is Rivet Beef Jerky.
The flavours we offer have been named Porch Lope, Ember Glaze and Chili Knack.
The Rivet Beef Jerky Title should remain the same across the three labels but the design for each flavour can change as you see fit.
Label needs to fit within 110mm x 110mm to suit our current packaging

Industry/Entity Type

Food Production

Logo Text

Morvendale Apiary

Colors

Designer to choose colors to be used in the design.

Requirements
Must have
• "Rivet Beef Jerky" font and colour must remain the same across the 3 designs
Nice to have
• The labels will be used on the clear side of the packaging with a small space towards the bottom being left visible so the product inside can be seen

```html
<!DOCTYPE html>
<html lang="en">
<head>
<meta charset="utf-8">
<title>Rivet Beef Jerky – Chili Knack Label</title>
<link rel="stylesheet" href="https://fonts.googleapis.com/css2?family=Bungee&family=Arvo:wght@700&display=swap">
<style>
  :root {
    --page-bg: #ffffff;
    --wood-light: #bdbdbd;
    --wood-mid: #a3a3a3;
    --wood-dark: #8a8a8a;
    --pennant-orange: #eaa03c;
    --pennant-edge: #d98a26;
    --stitch: #fff6e6;
    --ink: #1b1b1b;
    --ribbon-face: #ececec;
    --ribbon-shade: #9c9c9c;
    --window-dark: #4d4d4d;
    --window-deep: #3d3d3d;
    --silhouette: #141414;
  }
  html, body {
    margin: 0;
    padding: 0;
    width: 1200px;
    height: 904px;
    overflow: hidden;
    background: var(--page-bg);
  }
  .label-canvas {
    display: block;
    width: 1200px;
    height: 904px;
  }
  .brand-title {
    font-family: "Bungee", sans-serif;
    font-size: 50px;
    fill: var(--ink);
    letter-spacing: 2px;
  }
  .flavour-name {
    font-family: "Arvo", serif;
    font-weight: 700;
    font-size: 31px;
    fill: var(--ink);
    letter-spacing: 1px;
  }
</style>
</head>
<body>
<svg class="label-canvas" viewBox="0 0 1200 904" xmlns="http://www.w3.org/2000/svg">
  <defs>
    <linearGradient id="wood-tone" x1="0" y1="0" x2="1" y2="0">
      <stop offset="0" stop-color="var(--wood-dark)"/>
      <stop offset="0.35" stop-color="var(--wood-light)"/>
      <stop offset="0.7" stop-color="var(--wood-mid)"/>
      <stop offset="1" stop-color="var(--wood-dark)"/>
    </linearGradient>
    <linearGradient id="window-tone" x1="0" y1="0" x2="0" y2="1">
      <stop offset="0" stop-color="var(--window-dark)"/>
      <stop offset="1" stop-color="var(--window-deep)"/>
    </linearGradient>
  </defs>

  <!-- label background -->
  <rect class="wood-backdrop" x="415" y="68" width="420" height="780"
        fill="url(#wood-tone)" role="img" aria-label="Weathered grey wooden plank texture"/>

  <!-- clear product window -->
  <polygon class="product-window" points="415,505 627,640 835,505 835,738 415,738"
           fill="url(#window-tone)"/>

  <!-- orange pennant -->
  <g class="title-pennant">
    <polygon points="512,68 742,68 742,338 627,410 512,338" fill="var(--pennant-orange)"/>
    <polyline points="742,68 742,338 627,410" fill="none" stroke="var(--pennant-edge)" stroke-width="3"/>
    <polyline points="524,68 524,332 627,396 730,332 730,68" fill="none"
              stroke="var(--stitch)" stroke-width="2" stroke-dasharray="6 5"/>
    <text class="brand-title" x="627" y="200" text-anchor="middle">RIVET</text>
    <text class="brand-title" x="627" y="258" text-anchor="middle">BEEF</text>
    <text class="brand-title" x="627" y="316" text-anchor="middle">JERKY</text>
  </g>

  <!-- flavour ribbon -->
  <g class="flavour-ribbon">
    <polygon points="450,437 500,428 512,466 470,468" fill="var(--ribbon-shade)"/>
    <polygon points="805,437 755,428 743,466 785,468" fill="var(--ribbon-shade)"/>
    <path d="M492,420 Q627,400 762,420 L762,458 Q627,440 492,458 Z"
          fill="var(--ribbon-face)" stroke="var(--ink)" stroke-width="2"/>
    <text class="flavour-name" x="627" y="450" text-anchor="middle">CHILI KNACK</text>
  </g>

  <!-- animal emblem area -->
  <rect class="emblem-silhouette" x="548" y="484" width="137" height="116" rx="6"
        fill="var(--silhouette)" role="img" aria-label="Black silhouette of a buffalo"/>
</svg>
</body>
</html>
```